Marketing Flyer for Plumber Referals

8.5" x11" Layout should be landscape not portrait. Create a bold, eye-catching flyer that highlights earning potential from referrals for water damage restoration. Use high-contrast colors like blue, yellow, and white, with bold fonts and dynamic layouts. Include images of restoration work, cash, and happy clients. Emphasize key benefits like $500 minimum payouts, fast payments, and unlimited income potential. Keep instructions simple: refer a client, we handle the work, you get paid. Add a clear call-to-action and display contact details prominently. Focus on professionalism and energy.

Target Market(s)

Plumbers and Contractor 8.5" x11" Layout should be landscape not portrait.

Industry/Entity Type

General Contractor

Colors
0054AA
0677BA
7BADD7
CADEEF
E8F1F8
EB3D1F
EC4F4E
F09395
F8D3D4
FCEDEE

Requirements
Must have
• 8.5" x11" Layout should be landscape not portrait.
Nice to have

```html
<!DOCTYPE html>
<html lang="en">
<head>
<meta charset="utf-8">
<title>Referral Flyer – Harbor Crest Builders</title>
<link rel="stylesheet" href="https://fonts.googleapis.com/css2?family=Anton&family=Oswald:wght@500;600;700&family=Poppins:wght@400;600;700;800&family=Righteous&display=swap">
<style>
  :root{
    --frame:#2a2a2a;
    --paper:#ffffff;
    --red:#e5402a;
    --red-deep:#c9302a;
    --blue-light:#cadeef;
    --ink:#111111;
    --gray-panel:#e6e6e6;
    --slate:#2e3a50;
    --ring:#c3ccd0;
    --yellow:#f2d935;
  }
  *{box-sizing:border-box;margin:0;padding:0}
  html,body{width:1200px;height:856px;overflow:hidden;background:var(--frame)}
  .canvas{position:relative;width:1200px;height:856px;background:var(--frame)}
  .page{position:absolute;top:23px;width:579px;height:811px;background:var(--paper);overflow:hidden}
  .page--front{left:16px}
  .page--back{left:600px;background:linear-gradient(180deg,#fff 0,#fff 77px,#f1f1f1 78px,#ececec 420px,#fff 421px)}
  .abs{position:absolute}

  .brand{position:absolute;font-family:"Poppins",sans-serif;font-weight:600;font-size:10.5px;letter-spacing:.6px;color:var(--ink);text-transform:uppercase;display:flex;align-items:center;gap:6px;z-index:3}
  .brand__dot{width:9px;height:9px;background:var(--ink)}

  /* front */
  .hero-photo{left:0;top:0;width:579px;height:400px}
  .benefit-band{left:0;top:394px;width:300px;height:98px;background:var(--red)}
  .benefit{position:absolute;left:20px;display:flex;gap:8px;color:#fff;font-family:"Oswald",sans-serif;font-weight:600;font-size:16px;line-height:17px;letter-spacing:-.2px;z-index:2}
  .benefit svg{flex:none;margin-top:-2px}
  .cash-banner{left:0;top:0;width:579px;height:811px;pointer-events:none}
  .cash-banner__title{position:absolute;left:300px;top:405px;width:279px;text-align:center;font-family:"Anton",sans-serif;font-size:30px;line-height:36px;color:#fff;letter-spacing:.2px;white-space:nowrap}
  .cash-banner__sub{position:absolute;left:300px;top:446px;width:279px;text-align:center;font-family:"Anton",sans-serif;font-size:22px;line-height:28px;color:var(--blue-light);transform:skewX(-10deg);white-space:nowrap}
  .why-panel{left:0;top:531px;width:579px;height:187px;background:var(--gray-panel)}
  .why-tab{left:0;top:0;width:579px;height:811px;pointer-events:none}
  .why-tab__label{position:absolute;left:34px;top:517px;font-family:"Poppins",sans-serif;font-weight:800;font-size:18px;color:#fff;line-height:33px;z-index:2}
  .why-list{position:absolute;left:39px;top:580px;width:275px;font-family:"Poppins",sans-serif;font-size:12px;line-height:16px;color:#333;z-index:2}
  .why-list b{font-weight:700;color:#222}
  .client-photo{left:318px;top:515px;width:250px;height:223px;border-radius:110px 110px 0 0;background:linear-gradient(180deg,#7a5236 0,#8a5e40 45%,#e8443a 46%,#d8382f 100%)}
  .footer{position:absolute;left:0;top:738px;width:579px;height:73px;background:linear-gradient(90deg,var(--red),var(--red-deep));display:flex;align-items:center}
  .footer__cta{width:100%;text-align:center;font-family:"Anton",sans-serif;font-size:27px;color:#fff;letter-spacing:.2px}

  /* back */
  .headline{left:33px;top:128px;font-family:"Anton",sans-serif;font-size:43px;line-height:48px;color:var(--ink);letter-spacing:.3px}
  .steps-bar{left:27px;top:200px;width:370px;height:150px}
  .steps-label{position:absolute;top:318px;width:120px;text-align:center;font-family:"Righteous",sans-serif;font-size:22px;color:#fff;text-transform:lowercase}
  .advisor-photo{left:392px;top:172px;width:187px;height:239px;background:linear-gradient(180deg,#ecebe8 0,#e3dcd4 55%,#d9c8b4 100%)}
  .tech-photo{left:0;top:395px;width:250px;height:343px;border-radius:110px 110px 0 0;background:linear-gradient(180deg,#b98a6a 0,#b98a6a 30%,#2d52b8 31%,#1f3f9c 100%)}
  .works-title{position:absolute;left:290px;top:421px;width:260px;text-align:center;font-family:"Poppins",sans-serif;font-weight:800;font-size:32px;line-height:46px;color:#fff}
  .step-num{position:absolute;font-family:"Poppins",sans-serif;font-weight:600;font-size:31px;line-height:32px;color:#fff;-webkit-text-stroke:1.5px #2a2a2a;letter-spacing:-1px}
  .step-title{position:absolute;font-family:"Poppins",sans-serif;font-weight:700;font-size:12.3px;line-height:16px;color:#222;white-space:nowrap}
  .step-text{position:absolute;font-family:"Poppins",sans-serif;font-size:12.2px;line-height:16px;color:#333;padding-left:14px}
  .step-text::before{content:"•";position:absolute;left:2px;font-size:10px}
  .contact{position:absolute;left:0;top:738px;width:579px;height:73px;background:linear-gradient(90deg,var(--red),var(--red-deep));display:flex;align-items:center;gap:10px;padding-left:31px;color:#fff}
  .contact__web{font-family:"Poppins",sans-serif;font-weight:600;font-size:23px}
  .contact__phone{font-family:"Anton",sans-serif;font-size:33px;letter-spacing:.3px}
</style>
</head>
<body>
<div class="canvas">

  <section class="page page--front">
    <svg class="abs hero-photo" viewBox="0 0 579 400" role="img" aria-label="Photo of a flooded home interior with a leaking pipe and staircase">
      <defs>
        <linearGradient id="flood" x1="0" y1="0" x2="0" y2="1">
          <stop offset="0" stop-color="#c9c6bf"/>
          <stop offset=".5" stop-color="#9a9a98"/>
          <stop offset="1" stop-color="#5e6262"/>
        </linearGradient>
      </defs>
      <polygon points="0,77 255,77 284,40 579,40 579,400 0,400" fill="url(#flood)"/>
    </svg>
    <div class="brand" style="left:58px;top:58px"><span class="brand__dot"></span>Harbor Crest Builders</div>

    <div class="abs benefit-band"></div>
    <svg class="cash-banner abs" viewBox="0 0 579 811" aria-hidden="true">
      <defs>
        <linearGradient id="bannerBlue" x1="0" y1="0" x2="0" y2="1">
          <stop offset="0" stop-color="#3a57bf"/>
          <stop offset="1" stop-color="#26378a"/>
        </linearGradient>
      </defs>
      <polygon points="258,384 579,384 579,509 295,509" fill="url(#bannerBlue)"/>
    </svg>
    <div class="benefit" style="top:414px">
      <svg width="20" height="20" viewBox="0 0 24 24" fill="none" stroke="#fff" stroke-width="2" stroke-linejoin="round"><path d="M7 10v11H3V10h4zm0 0 4-8c2 0 3 1 2.5 3L13 9h6a2 2 0 0 1 2 2.3l-1.3 7.4A2 2 0 0 1 17.7 21H7"/></svg>
      <span>$500 Minimum or 10% Per Referral!</span>
    </div>
    <div class="benefit" style="top:442px">
      <svg width="20" height="20" viewBox="0 0 24 24" fill="none" stroke="#fff" stroke-width="2" stroke-linejoin="round"><path d="M7 10v11H3V10h4zm0 0 4-8c2 0 3 1 2.5 3L13 9h6a2 2 0 0 1 2 2.3l-1.3 7.4A2 2 0 0 1 17.7 21H7"/></svg>
      <span>Partner with the<br>#1 Water Damage Restoration Team</span>
    </div>
    <div class="cash-banner__title">EARN UNLIMITED CASH</div>
    <div class="cash-banner__sub">GET PAID TO REFER A FLOOD</div>

    <div class="abs why-panel"></div>
    <div class="abs client-photo" role="img" aria-label="Photo of a smiling client in a red t-shirt looking upward"></div>
    <svg class="why-tab abs" viewBox="0 0 579 811" aria-hidden="true">
      <defs>
        <linearGradient id="tabBlue" x1="0" y1="0" x2="0" y2="1">
          <stop offset="0" stop-color="#3a57bf"/>
          <stop offset="1" stop-color="#26378a"/>
        </linearGradient>
      </defs>
      <polygon points="0,517 287,517 268,550 0,550" fill="url(#tabBlue)"/>
      <polygon points="274,531 287,517 299,531" fill="#111"/>
    </svg>
    <div class="why-tab__label">Why Partner with Us?</div>
    <div class="why-list">
      <p><b>Guaranteed Payout:</b> Minimum $500 or 10% of the invoice, paid fast.</p>
      <p><b>Free Evaluations:</b> We assess damage and process insurance claims for your clients.</p>
      <p><b>Industry Leaders:</b> Certified experts with 24/7 rapid response.</p>
      <p><b>Affordable Solutions:</b> Lowest out-of-pocket costs for your customers.</p>
    </div>

    <div class="footer"><div class="footer__cta">SEND REFERRALS. GET PAID. GROW YOUR BUSINESS</div></div>
  </section>

  <section class="page page--back">
    <div class="brand" style="right:70px;top:62px"><span class="brand__dot"></span>Harbor Crest Builders</div>
    <div class="abs headline">GET PAID TO REFER A FLOOD</div>

    <svg class="abs steps-bar" viewBox="0 0 370 150" aria-hidden="true">
      <path d="M0,67 H370 V132 L362,147 H8 L0,132 Z" fill="var(--slate)"/>
      <circle cx="64" cy="57" r="57" fill="#fff" stroke="var(--ring)" stroke-width="6"/>
      <circle cx="64" cy="57" r="47" fill="#dfe4e6"/>
      <circle cx="185" cy="57" r="57" fill="#fff" stroke="#dfe4e6" stroke-width="6"/>
      <circle cx="185" cy="57" r="47" fill="#e4e9ea"/>
      <circle cx="306" cy="57" r="57" fill="#fff" stroke="var(--yellow)" stroke-width="6"/>
      <text x="306" y="84" text-anchor="middle" font-family="Anton, sans-serif" font-size="78" fill="var(--yellow)">$</text>
    </svg>
    <div class="steps-label" style="left:31px">join</div>
    <div class="steps-label" style="left:152px">promote</div>
    <div class="steps-label" style="left:273px;color:var(--yellow)">earn</div>

    <div class="abs advisor-photo" role="img" aria-label="Photo of a thoughtful businesswoman in a beige blazer"></div>

    <svg class="abs" style="left:0;top:0" width="579" height="811" viewBox="0 0 579 811" aria-hidden="true">
      <defs>
        <linearGradient id="bandBlue" x1="0" y1="0" x2="0" y2="1">
          <stop offset="0" stop-color="#3a57bf"/>
          <stop offset="1" stop-color="#26378a"/>
        </linearGradient>
      </defs>
      <polygon points="0,389 267,389 273,404 230,509 0,509" fill="url(#bandBlue)"/>
      <polygon points="252,411 579,411 579,478 239,478" fill="var(--red)"/>
      <polygon points="290,738 579,738 579,640" fill="#e4e4e4"/>
    </svg>
    <div class="abs tech-photo" role="img" aria-label="Photo of a smiling technician in blue coveralls holding a wrench"></div>
    <div class="works-title">How It Works</div>

    <div class="step-num" style="left:391px;top:489px">01</div>
    <div class="step-title" style="left:301px;top:527px">Refer Flood, Water and Mold Damage</div>
    <div class="step-text" style="left:305px;top:543px">Call, book online, or text us directly.</div>

    <div class="step-num" style="left:391px;top:566px">02</div>
    <div class="step-title" style="left:291px;top:600px">We Take Care of Everything</div>
    <div class="step-text" style="left:291px;top:616px;width:275px">Free evaluations, insurance claims, and professional service.</div>

    <div class="step-num" style="left:391px;top:652px">03</div>
    <div class="step-title" style="left:291px;top:673px">Get Paid Fast</div>
    <div class="step-text" style="left:291px;top:689px;width:275px">$500 minimum or 10% of the invoice within 48 hours of final payment.</div>

    <div class="contact">
      <span class="contact__web">HarborCrestRestore.com</span>
      <svg width="30" height="30" viewBox="0 0 30 30" aria-hidden="true">
        <circle cx="15" cy="15" r="13" fill="none" stroke="#fff" stroke-width="3"/>
        <path d="M10 8.5c.6-.6 1.5-.5 1.9.2l1.3 2.2c.3.6.2 1.3-.3 1.7l-.9.7c.7 1.6 2 2.9 3.6 3.6l.7-.9c.4-.5 1.1-.6 1.7-.3l2.2 1.3c.7.4.8 1.3.2 1.9l-1 1c-.9.9-2.3 1.1-3.5.5-3.2-1.5-5.8-4.1-7.3-7.3-.5-1.2-.3-2.6.5-3.5z" fill="#fff"/>
      </svg>
      <span class="contact__phone">555-214-7730</span>
    </div>
  </section>

</div>
</body>
</html>
```